Business card design for strategy and management consulting company. Would like to have a clean and professional business card, based on the attached logo. The company is a strategy and management consulting company focusing on sustainable business modlels based on economic, social and environmental market opportunities. Preferably the logo should be included on both sides of the design.

Industry/Entity Type

Business

Contact Information for Business Card

Halvor Brekkeli, CEO/Management consultant
halvor.brekkeli@morvikpartners.example
Mob: +47 936 28 417
Office: Lyngvedens gate 14, pb 312 sentrum, N-0158 Oslo Norway

Requirements
Must have
• Include attached logo
Nice to have
• Would like to have the logo on both sides
Should not have
• Many colours.

```html
<!DOCTYPE html>
<html lang="en">
<head>
<meta charset="utf-8">
<title>Morvik business card</title>
<link rel="stylesheet" href="https://fonts.googleapis.com/css2?family=Source+Sans+3:wght@400;600;700&display=swap">
<style>
  :root {
    --backdrop: #4a423d;
    --card: #161616;
    --card-edge: #222222;
    --gloss: #8d8d8d;
    --muted: #9a9a9a;
    --white: #f4f4f4;
    --accent: #f5c518;
    --rule: #6d6d6d;
  }
  * { margin: 0; padding: 0; box-sizing: border-box; }
  html, body {
    width: 1200px;
    height: 864px;
    overflow: hidden;
    background: var(--backdrop);
    font-family: "Source Sans 3", "Helvetica Neue", Arial, sans-serif;
  }
  .sheet {
    width: 1200px;
    height: 864px;
    display: flex;
    align-items: center;
    justify-content: center;
    gap: 40px;
  }
  .card {
    position: relative;
    width: 540px;
    height: 309px;
    background: var(--card);
    border: 1px solid var(--card-edge);
    box-shadow: 0 14px 30px rgba(0,0,0,.35);
    overflow: hidden;
  }

  /* Company name */
  .brand {
    font-weight: 700;
    line-height: 1;
    white-space: nowrap;
  }

  /* Front */
  .card--front {
    display: flex;
    flex-direction: column;
    align-items: center;
    justify-content: center;
  }
  .card--front .brand { font-size: 88px; color: var(--gloss); }
  .front__web {
    margin-top: 34px;
    font-size: 13px;
    letter-spacing: 4px;
    color: var(--muted);
  }

  /* Back */
  .card--back .brand {
    position: absolute;
    left: 34px;
    top: 120px;
    font-size: 58px;
    color: var(--white);
  }
  .back__rule {
    position: absolute;
    left: 262px;
    top: 96px;
    width: 1px;
    height: 170px;
    background: var(--rule);
  }
  .details {
    position: absolute;
    left: 280px;
    top: 94px;
    width: 250px;
    color: var(--white);
    font-size: 13px;
    line-height: 1.28;
  }
  .details__name {
    color: var(--accent);
    font-weight: 700;
    font-size: 15px;
    text-transform: uppercase;
    letter-spacing: .3px;
  }
  .details__title { text-transform: uppercase; }
  .details__address { margin-top: 6px; }
  .contact {
    list-style: none;
    margin-top: 4px;
  }
  .contact li {
    display: flex;
    align-items: center;
    gap: 7px;
    font-size: 12px;
    white-space: nowrap;
  }
  .contact svg {
    width: 11px;
    height: 11px;
    flex: none;
  }
</style>
</head>
<body>
<main class="sheet">
  <section class="card card--front" aria-label="Card front">
    <p class="brand">Morvik</p>
    <p class="front__web">www.morvikpartners.example</p>
  </section>

  <section class="card card--back" aria-label="Card back">
    <p class="brand">Morvik</p>
    <div class="back__rule"></div>
    <div class="details">
      <p class="details__name">Halvor Brekkeli</p>
      <p class="details__title">CEO/Management<br>Consultant</p>
      <p class="details__address">Lyngvedens gate 14,<br>pb 312 sentrum, N-0158 Oslo Norway</p>
      <ul class="contact">
        <li>
          <svg viewBox="0 0 12 12" aria-hidden="true"><rect x="3" y="0.5" width="6" height="11" rx="1.2" fill="none" stroke="var(--accent)" stroke-width="1.3"/><circle cx="6" cy="9.5" r=".8" fill="var(--accent)"/></svg>
          <span>+47 936 28 417</span>
        </li>
        <li>
          <svg viewBox="0 0 12 12" aria-hidden="true"><rect x=".5" y="2" width="11" height="8" fill="var(--accent)"/><path d="M.5 2 6 6.5 11.5 2" fill="none" stroke="var(--card)" stroke-width="1"/></svg>
          <span>halvor.brekkeli@morvikpartners.example</span>
        </li>
        <li>
          <svg viewBox="0 0 12 12" aria-hidden="true"><circle cx="6" cy="6" r="5.5" fill="var(--accent)"/><path d="M6 3v3.2h2.4" fill="none" stroke="var(--card)" stroke-width="1.2"/></svg>
          <span>www.morvikpartners.example</span>
        </li>
      </ul>
    </div>
  </section>
</main>
</body>
</html>
```